Physical Therapy Center for children Business Card

We need a Business Card for our company (Physical Therapy for children and youth with special needs) in Lisbon, Portugal. The name of the company is "Ninho de Luz"

The card must contain the following info:
- Logo: see uploaded file
- Name: Ninho de Luz
- Slogan: Plantamos carinho, vemos crescer, celebramos conquistas!
- Service: Terapias Especializadas
- Address: Rua Henrique Lobato Farinha 9C
- ZipCode: 2741-318 Vila Serena do Tejo
- E-mail: geral@velado.pt
- Site: www.velado.pt
- Facebook: www.facebook.com/ninhodeluz
- Phone: +351 21 584 62 07
- Cell Phone: +351 96 731 84 25

The stationary should have contain all info from business card.

Target Market(s)

Parents of children with special needs

Industry/Entity Type

Physical Therapy

Contact Information for Business Card

The card design should be compatible with http://www.quellprensa.com/product2/order_detail.php?gid=40

Requirements
Should not have
• The business card should not have a Black background. Use white or other color.

```html
<!DOCTYPE html>
<html lang="pt">
<head>
<meta charset="utf-8">
<title>Ninho de Luz — Papel de Carta</title>
<link rel="stylesheet" href="https://fonts.googleapis.com/css2?family=Open+Sans:wght@400;600&family=Raleway:wght@400&family=Tinos:wght@400;700&display=swap">
<style>
  :root {
    --brand-red: #e8453f;
    --brand-teal: #2bb5a4;
    --paper: #ffffff;
    --ink: #111111;
    --mark-faint: #f1f1f1;
    --name-ink: #3a3a3a;
  }
  html, body {
    margin: 0;
    padding: 0;
    width: 864px;
    height: 1200px;
    overflow: hidden;
    background: var(--paper);
  }
  .letterhead {
    position: relative;
    width: 864px;
    height: 1200px;
    background: var(--paper);
    overflow: hidden;
  }
  .header-band {
    position: absolute;
    left: 0; top: 0;
    width: 525px; height: 95px;
    background: var(--brand-red);
  }
  .header-slogan {
    position: absolute;
    left: 52px; top: 21px;
    margin: 0;
    font-family: "Open Sans", sans-serif;
    font-size: 13.5px;
    line-height: 18px;
    color: #fff;
    text-transform: uppercase;
    letter-spacing: -0.2px;
  }
  .header-service {
    position: absolute;
    left: 52px; top: 68px;
    margin: 0;
    font-family: "Open Sans", sans-serif;
    font-size: 13.5px;
    color: #fff;
    text-transform: uppercase;
    letter-spacing: -0.2px;
  }
  .brand-dot {
    position: absolute;
    left: 530px; top: 32px;
    width: 30px; height: 30px;
    border-radius: 50%;
    background: var(--brand-teal);
  }
  .brand-name {
    position: absolute;
    left: 592px; top: 57px;
    margin: 0;
    font-family: "Raleway", sans-serif;
    font-weight: 400;
    font-size: 30px;
    line-height: 34px;
    color: var(--name-ink);
    white-space: nowrap;
  }
  .backdrop-mark {
    position: absolute;
    left: 250px; top: 330px;
    width: 340px; height: 340px;
    border-radius: 50%;
    background: var(--mark-faint);
  }
  .letter-text {
    position: absolute;
    left: 53px;
    width: 773px;
    margin: 0;
    font-family: "Tinos", "Times New Roman", serif;
    font-size: 18px;
    line-height: 21px;
    color: var(--ink);
  }
  .letter-text sup { font-size: 11px; line-height: 0; }
  .recipient { top: 163px; }
  .reference { top: 292px; font-weight: 700; }
  .salutation { top: 377px; }
  .paragraph-one { top: 420px; text-align: justify; }
  .paragraph-two { top: 505px; text-align: justify; }
  .acknowledge { top: 590px; }
  .closing { top: 676px; }
  .footer-band {
    position: absolute;
    left: 56px; top: 1104px;
    width: 808px; height: 96px;
    background: var(--brand-red);
  }
  .footer-dot {
    position: absolute;
    left: 46px; top: 1106px;
    width: 48px; height: 48px;
    border-radius: 50%;
    background: var(--brand-teal);
  }
  .footer-address {
    position: absolute;
    left: 128px; top: 1126px;
    margin: 0;
    font-family: "Open Sans", sans-serif;
    font-size: 10px;
    line-height: 14px;
    color: #fff;
  }
  .footer-social {
    position: absolute;
    left: 128px; top: 1169px;
    display: flex; align-items: center; gap: 6px;
    font-family: "Open Sans", sans-serif;
    font-size: 11px;
    color: #fff;
  }
  .footer-social .square {
    width: 10px; height: 10px; background: #fff; border-radius: 2px;
  }
  .footer-contacts {
    position: absolute;
    right: 52px; top: 1126px;
    margin: 0; padding: 0;
    list-style: none;
    font-family: "Open Sans", sans-serif;
    font-size: 10px;
    line-height: 15.5px;
    color: #fff;
    text-align: right;
  }
  .footer-contacts li { display: flex; justify-content: flex-end; align-items: center; gap: 5px; }
  .footer-contacts svg { width: 8px; height: 8px; fill: #fff; }
</style>
</head>
<body>
<main class="letterhead">
  <div class="header-band"></div>
  <p class="header-slogan">Plantamos carinho, vemos crescer,<br>celebramos conquistas!</p>
  <p class="header-service">Terapias Especializadas</p>
  <div class="brand-dot"></div>
  <p class="brand-name">Ninho de Luz</p>

  <div class="backdrop-mark"></div>

  <p class="letter-text recipient">Name of employee: Mr. xyz<br>Address of employee<br>address line 2</p>
  <p class="letter-text reference">Ref: Promotion as an Assistant secretary</p>
  <p class="letter-text salutation">Dear Mr. xyz,</p>
  <p class="letter-text paragraph-one">I have the pleasure to inform you that you have been promoted as assistant secretary in the share department of the company. You are required to take charge of the new assignment on 15<sup>th</sup> May, 2012. Please accept my hearty congratulations on your promotion.</p>
  <p class="letter-text paragraph-two">Your salary scale in the promoted cadre will be Tk. 16,000 and from 15th may, your basic salary will be fixed at Tk. 12,000 in the said scale. You will be entitled to all other allowances as applicable to the staff-II of the company. Other services conditions remain unchanged.</p>
  <p class="letter-text acknowledge">Please acknowledge receipt of this letter.</p>
  <p class="letter-text closing">Yours sincerely,</p>

  <div class="footer-band"></div>
  <div class="footer-dot"></div>
  <p class="footer-address">Rua Henrique Lobato Farinha 9C<br>2741-318 Vila Serena do Tejo</p>
  <div class="footer-social"><span class="square"></span>ninhodeluz</div>
  <ul class="footer-contacts">
    <li>+351 21 584 62 07 <svg viewBox="0 0 8 8"><rect x="2" y="0" width="4" height="8" rx="1"/></svg></li>
    <li>+351 96 731 84 25 <svg viewBox="0 0 8 8"><path d="M0 3 Q4 0 8 3 L6 4 L5 3 L3 3 L2 4 Z M1 5 H7 V8 H1 Z"/></svg></li>
    <li>geral@velado.pt <svg viewBox="0 0 8 8"><rect x="0" y="1.5" width="8" height="5"/></svg></li>
    <li>www.velado.pt <svg viewBox="0 0 8 8"><circle cx="4" cy="4" r="4"/></svg></li>
  </ul>
</main>
</body>
</html>
```